Flyer for a Payroll and Bookkeeping Companmy

Need a brochure to highlight our costs and service to hand out to clients.

Please see attachments for more information.

It Service

```html
<!DOCTYPE html>
<html lang="en">
<head>
<meta charset="utf-8">
<title>Northpeak Ledger – Pricing Flyer</title>
<link href="https://fonts.googleapis.com/css2?family=Montserrat:wght@800;900&family=Oswald:wght@400;500&family=Open+Sans:wght@400;600;700&family=Source+Sans+3:wght@700&display=swap" rel="stylesheet">
<style>
:root{
  --blue:#1565b0;
  --blue-dark:#0f4f8f;
  --orange:#e9892a;
  --orange-deep:#dd5a1c;
  --gold:#eba12c;
  --ink:#222;
  --cell-gray:#d9d9d9;
  --stage:#e2e2e2;
}
*{box-sizing:border-box;margin:0;padding:0}
html,body{width:1200px;height:817px;overflow:hidden}
body{background:var(--stage);font-family:"Open Sans",sans-serif;color:var(--ink);position:relative}
.side-label{position:absolute;top:38px;width:483px;text-align:center;font:700 16px/1 "Open Sans",sans-serif;letter-spacing:1px;color:#1d1d1d}
.flyer{position:absolute;top:68px;width:483px;height:676px;background:linear-gradient(180deg,#f4f4f4,#e9e9e9);overflow:hidden;box-shadow:0 2px 8px rgba(0,0,0,.18)}
.flyer--front{left:94px}
.flyer--back{left:615px}
.header{position:absolute;top:0;left:0;width:483px;height:132px}
.brand{position:absolute;top:58px;left:0;width:483px;text-align:center}
.brand-name{display:inline-flex;align-items:center;gap:6px;font:700 20px/1 "Source Sans 3",sans-serif;color:var(--blue)}
.brand-dot{width:12px;height:12px;border-radius:50%;background:var(--orange)}
.brand-tag{font:600 11px/1 "Open Sans",sans-serif;color:var(--orange);margin-top:4px}
.title{position:absolute;left:0;width:483px;text-align:center;font-family:"Montserrat",sans-serif;font-weight:900;white-space:nowrap}
.title--bookkeeping{top:160px;font-size:28px;color:var(--blue)}
.title--bookkeeping span{color:var(--orange)}
.title--simplified{top:163px;font-size:49px;color:var(--blue);line-height:1}
.title--payroll{top:213px;font-size:30px;color:var(--orange);line-height:1}
.title-rule{position:absolute;left:70px;width:343px;height:1px;background:linear-gradient(90deg,transparent,#c9c9c9,transparent)}

/* pricing table */
.pricing{position:absolute;left:36px;top:222px;width:414px}
.pricing-head{display:grid;grid-template-columns:86px repeat(4,1fr);height:67px;box-shadow:0 2px 4px rgba(0,0,0,.25)}
.pricing-head .services{background:var(--blue);color:#fff;font:400 13px/67px "Oswald",sans-serif;text-align:center}
.plan{color:#fff;text-align:center;font-family:"Oswald",sans-serif}
.plan-name{font-size:11px;height:22px;line-height:22px;background:rgba(0,0,0,.06)}
.plan-price{font-size:23px;line-height:42px;font-weight:500}
.plan--premium{background:var(--gold)}
.plan--entrepreneur{background:#e8902a}
.plan--growth{background:#e27424}
.plan--startup{background:var(--orange-deep)}
.pricing-row{display:grid;grid-template-columns:86px repeat(4,1fr);height:26.5px;align-items:center;font-size:6px;line-height:1.15;text-align:center}
.pricing-row > div{height:25px;display:flex;flex-direction:column;align-items:center;justify-content:center}
.pricing-row .label{align-items:flex-start;text-align:left;font-weight:700;font-size:5.2px;padding-left:5px;line-height:1.25;white-space:nowrap}
.pricing-row.alt .label{background:var(--blue);color:#fff;margin-left:5px}
.pricing-row.alt .c2,.pricing-row.alt .c4{background:var(--cell-gray);margin:0 1px}
.note{color:var(--orange);font-size:6px}
.tick{width:7px;height:7px;border-radius:50%;background:var(--orange);position:relative;display:inline-block}
.tick::after{content:"";position:absolute;left:2.2px;top:1.2px;width:1.6px;height:3px;border:solid #fff;border-width:0 1px 1px 0;transform:rotate(45deg)}

/* price circles */
.badge{position:absolute;top:278px;width:136px;height:136px;border-radius:50%;background:#fff;border:4px solid var(--orange);box-shadow:inset 0 0 0 7px #e2e2e2,0 10px 12px -8px rgba(0,0,0,.35);display:flex;flex-direction:column;align-items:center;justify-content:center;font-family:"Oswald",sans-serif;text-align:center}
.badge--blue{border-color:var(--blue)}
.badge-big{font-size:36px;line-height:1;font-weight:500;color:var(--orange)}
.badge-small{font-size:17px;line-height:1.2;color:#222;white-space:nowrap}
.badge--one{left:25px}.badge--two{left:167px}.badge--three{left:313px}
.payroll-note{position:absolute;top:442px;left:0;width:483px;text-align:center;font-size:13.4px;line-height:18px;color:#222;white-space:nowrap}
.payroll-note b{font-weight:700}

.photo{position:absolute;left:0;width:483px;background:linear-gradient(180deg,rgba(233,233,233,0),#d2d2d2 60%,#c6c6c6)}
.flyer--front .photo{top:500px;height:112px}
.flyer--back .photo{top:488px;height:124px}

/* footer */
.footer-band{position:absolute;top:612px;left:0;width:483px;height:24px;background:linear-gradient(90deg,var(--orange),var(--orange-deep))}
.footer-tab{position:absolute;top:612px;left:130px;width:223px;height:24px;background:var(--blue);clip-path:polygon(12px 0,100% 0,calc(100% - 12px) 100%,0 100%);color:#fff;font:700 11px/24px "Open Sans",sans-serif;letter-spacing:2.4px;text-align:center}
.footer-contact{position:absolute;top:636px;left:0;width:483px;height:40px;background:var(--blue-dark);display:flex;align-items:center;justify-content:center;gap:12px;color:#fff;font-size:9.6px;white-space:nowrap}
.contact-item{display:flex;align-items:center;gap:5px}
.contact-icon{width:10px;height:10px;border-radius:50%;background:var(--orange);display:flex;align-items:center;justify-content:center}
</style>
</head>
<body>

<div class="side-label" style="left:94px">FLYER FRONT</div>
<div class="side-label" style="left:615px">FLYER BACK</div>

<!-- FRONT -->
<section class="flyer flyer--front">
  <svg class="header" viewBox="0 0 483 132" aria-hidden="true">
    <rect width="483" height="132" fill="#efefef"/>
    <polygon points="0,80 483,80 483,132 0,132" fill="#e9892a"/>
    <polygon points="0,0 60,0 165,108 0,108" fill="#1565b0"/>
    <polygon points="483,0 423,0 318,108 483,108" fill="#1565b0"/>
    <polygon points="0,80 96,80 122,108 0,108" fill="#1870c0"/>
    <polygon points="483,80 387,80 361,108 483,108" fill="#1870c0"/>
    <polygon points="0,108 165,108 178,132 0,132" fill="#e97f24"/>
    <polygon points="483,108 318,108 305,132 483,132" fill="#e97f24"/>
    <polygon points="130,108 353,108 340,132 143,132" fill="#eda039"/>
    <polyline points="110,120 218,120" stroke="#fff" stroke-width="0.7" fill="none"/>
    <polyline points="262,120 372,120 384,108" stroke="#fff" stroke-width="0.7" fill="none"/>
    <circle cx="218" cy="120" r="2.5" fill="#fff"/><circle cx="262" cy="120" r="2.5" fill="#fff"/>
    <polygon points="165,108 318,108 330,96 153,96" fill="#efefef"/>
    <polygon points="96,0 387,0 318,96 165,96" fill="#f4f4f4"/>
  </svg>
  <div class="brand">
    <div class="brand-name"><span class="brand-dot"></span>Northpeak Ledger</div>
    <div class="brand-tag">Payroll and Bookkeeping</div>
  </div>

  <h1 class="title title--bookkeeping">BOOKKEEPING <span>PRICING</span></h1>
  <div class="title-rule" style="top:204px"></div>

  <div class="pricing">
    <div class="pricing-head">
      <div class="services">SERVICES</div>
      <div class="plan plan--premium"><div class="plan-name">Premium</div><div class="plan-price">$999</div></div>
      <div class="plan plan--entrepreneur"><div class="plan-name">Entrepreneur</div><div class="plan-price">$599</div></div>
      <div class="plan plan--growth"><div class="plan-name">Growth</div><div class="plan-price">$299</div></div>
      <div class="plan plan--startup"><div class="plan-name">Start Up</div><div class="plan-price">$149</div></div>
    </div>
    <div class="pricing-row"><div class="label">Employees</div><div class="c1">Around<br>10+</div><div class="c2">Around<br>5-9</div><div class="c3">Around<br>2-5</div><div class="c4">Around<br>5-9</div></div>
    <div class="pricing-row alt"><div class="label">Transactions / Month</div><div class="c1">Up to<br>250</div><div class="c2">Up to<br>150</div><div class="c3">Up to<br>75</div><div class="c4">Up to<br>150</div></div>
    <div class="pricing-row"><div class="label">Bookkeeping</div><div class="c1"><span class="tick"></span><span class="note">Weekly</span></div><div class="c2"><span class="tick"></span><span class="note">Weekly</span></div><div class="c3"><span class="tick"></span><span class="note">Monthly</span></div><div class="c4"><span class="tick"></span><span class="note">Weekly</span></div></div>
    <div class="pricing-row alt"><div class="label">Financial Reports &amp; Review</div><div class="c1"><span class="tick"></span><span class="note">Monthly</span></div><div class="c2"><span class="tick"></span><span class="note">Monthly</span></div><div class="c3"><span class="tick"></span><span class="note">Monthly</span></div><div class="c4"><span class="tick"></span><span class="note">Monthly</span></div></div>
    <div class="pricing-row"><div class="label">Support (Phone and Chat)</div><div class="c1"><span class="tick"></span></div><div class="c2"><span class="tick"></span></div><div class="c3"><span class="tick"></span></div><div class="c4"><span class="tick"></span></div></div>
    <div class="pricing-row alt"><div class="label">Online Collaboration Portal<br>(Shared Folder)</div><div class="c1"><span class="tick"></span></div><div class="c2"><span class="tick"></span></div><div class="c3"><span class="tick"></span></div><div class="c4"><span class="tick"></span></div></div>
    <div class="pricing-row"><div class="label">Business Tax Return</div><div class="c1"><span class="tick"></span></div><div class="c2"><span class="tick"></span></div><div class="c3">$799</div><div class="c4"><span class="tick"></span></div></div>
    <div class="pricing-row alt"><div class="label">Bill Pay<br>(with Approval Process)</div><div class="c1"><span class="tick"></span><span class="note">$5 / Payment</span></div><div class="c2">x</div><div class="c3">x</div><div class="c4">x</div></div>
  </div>

  <div class="photo" role="img" aria-label="Faded desk photo with calculator, banknotes and financial charts"></div>

  <div class="footer-band"></div>
  <div class="footer-tab">GET IN TOUCH WITH US</div>
  <div class="footer-contact">
    <span class="contact-item"><span class="contact-icon"><svg width="6" height="7" viewBox="0 0 6 7"><path d="M3 0a2.2 2.2 0 0 0-2.2 2.2C.8 3.8 3 7 3 7s2.2-3.2 2.2-4.8A2.2 2.2 0 0 0 3 0z" fill="#fff"/></svg></span>1420 Harbor Row, Fairview, UT 84010</span>
    <span class="contact-item"><span class="contact-icon"><svg width="6" height="6" viewBox="0 0 6 6"><path d="M1 0l1.2 1.4-.6.9c.4.8 1.1 1.5 1.9 1.9l.9-.6L6 5 5 6C2.3 6 0 3.7 0 1z" fill="#fff"/></svg></span>555-014-2290</span>
    <span class="contact-item"><span class="contact-icon"><svg width="6" height="6" viewBox="0 0 6 6"><circle cx="3" cy="3" r="2.5" fill="none" stroke="#fff" stroke-width=".8"/><path d="M.5 3h5" stroke="#fff" stroke-width=".6"/></svg></span>www.northpeakledger.com</span>
  </div>
</section>

<!-- BACK -->
<section class="flyer flyer--back">
  <svg class="header" viewBox="0 0 483 132" aria-hidden="true">
    <rect width="483" height="132" fill="#efefef"/>
    <polygon points="0,80 483,80 483,132 0,132" fill="#e9892a"/>
    <polygon points="0,0 60,0 165,108 0,108" fill="#1565b0"/>
    <polygon points="483,0 423,0 318,108 483,108" fill="#1565b0"/>
    <polygon points="0,80 96,80 122,108 0,108" fill="#1870c0"/>
    <polygon points="483,80 387,80 361,108 483,108" fill="#1870c0"/>
    <polygon points="0,108 165,108 178,132 0,132" fill="#e97f24"/>
    <polygon points="483,108 318,108 305,132 483,132" fill="#e97f24"/>
    <polygon points="130,108 353,108 340,132 143,132" fill="#eda039"/>
    <polyline points="110,120 218,120" stroke="#fff" stroke-width="0.7" fill="none"/>
    <polyline points="262,120 372,120 384,108" stroke="#fff" stroke-width="0.7" fill="none"/>
    <circle cx="218" cy="120" r="2.5" fill="#fff"/><circle cx="262" cy="120" r="2.5" fill="#fff"/>
    <polygon points="165,108 318,108 330,96 153,96" fill="#efefef"/>
    <polygon points="96,0 387,0 318,96 165,96" fill="#f4f4f4"/>
  </svg>
  <div class="brand">
    <div class="brand-name"><span class="brand-dot"></span>Northpeak Ledger</div>
    <div class="brand-tag">Payroll and Bookkeeping</div>
  </div>

  <h1 class="title title--simplified">SIMPLIFIED</h1>
  <h2 class="title title--payroll">PAYROLL PRICING</h2>
  <div class="title-rule" style="top:255px"></div>

  <div class="badge badge--one"><div class="badge-big">$25</div><div class="badge-small">PER PAYROLL</div></div>
  <div class="badge badge--two badge--blue"><div class="badge-big">+$5</div><div class="badge-small">PER EMPLOYEE</div></div>
  <div class="badge badge--three"><div class="badge-small">NO SET UP</div><div class="badge-big">FEES</div></div>

  <p class="payroll-note">Direct deposit only, add <b>$20</b> per payroll if you elect to have<br>paper checks shipped to you.&nbsp; Minimum charge of two payrolls<br>per month.&nbsp; Cost per employee drops to <b>$4</b> after <b>20</b> employees.</p>

  <div class="photo" role="img" aria-label="Faded photo of a hand writing on documents beside a calculator"></div>

  <div class="footer-band"></div>
  <div class="footer-tab">GET IN TOUCH WITH US</div>
  <div class="footer-contact">
    <span class="contact-item"><span class="contact-icon"><svg width="6" height="7" viewBox="0 0 6 7"><path d="M3 0a2.2 2.2 0 0 0-2.2 2.2C.8 3.8 3 7 3 7s2.2-3.2 2.2-4.8A2.2 2.2 0 0 0 3 0z" fill="#fff"/></svg></span>1420 Harbor Row, Fairview, UT 84010</span>
    <span class="contact-item"><span class="contact-icon"><svg width="6" height="6" viewBox="0 0 6 6"><path d="M1 0l1.2 1.4-.6.9c.4.8 1.1 1.5 1.9 1.9l.9-.6L6 5 5 6C2.3 6 0 3.7 0 1z" fill="#fff"/></svg></span>555-014-2290</span>
    <span class="contact-item"><span class="contact-icon"><svg width="6" height="6" viewBox="0 0 6 6"><circle cx="3" cy="3" r="2.5" fill="none" stroke="#fff" stroke-width=".8"/><path d="M.5 3h5" stroke="#fff" stroke-width=".6"/></svg></span>www.northpeakledger.com</span>
  </div>
</section>

</body>
</html>
```